Finiding oppertunites in Real Estate 6.15.20

size of ad 7” x 9.6”
1-I like the ad to stand out and attract people's attention.
2-you should be able to see the text of the ad clearly .. see the attachment anything in yellow is instructions.
3-the list of topics should not be the main part of the ad
4-if you decide you want a picture or vector of a person .. (you decide)
then it should be a white male about 25-30 years old wearing a solid white or blue shirt and not long hair.
5-leave 1 inch for footer
see attachment
Good luck

Target Market(s)

potential male students 25-35 years of age

Industry/Entity Type

Education

Requirements
Must have
• will stand out and people would want to see it.
should be able to read the words of ad
Nice to have
• how to make money in real estate on one line

```html
<!DOCTYPE html>
<html lang="en">
<head>
<meta charset="utf-8">
<title>Real Estate Career Course Poster</title>
<link rel="stylesheet" href="https://fonts.googleapis.com/css2?family=Montserrat:wght@500;600;700;800&family=Oswald:wght@400;500;600&display=swap">
<style>
  :root {
    --page-bg: #d6d6d6;
    --poster-top: #e4e4e4;
    --poster-bottom: #fafafa;
    --header-band: #4a3a3a;
    --ink: #2b2b2b;
    --ink-soft: #3a3a3a;
    --accent-red: #9c1a1f;
    --blob-red: #a3171c;
    --white: #ffffff;
    --footer-rule: #1c1c1c;
    --photo-light: #f1f1f1;
    --photo-mid: #d9d9d9;
    --photo-shadow: #b9b9b9;
  }
  * { margin: 0; padding: 0; box-sizing: border-box; }
  html, body {
    width: 686px; height: 1200px; overflow: hidden;
    background: var(--page-bg);
  }
  .poster {
    position: absolute; left: 0; top: 129px;
    width: 686px; height: 941px; overflow: hidden;
    background: linear-gradient(180deg, var(--poster-top) 0%, var(--poster-bottom) 90%);
    font-family: "Montserrat", sans-serif;
    color: var(--ink);
  }
  .portrait-photo {
    position: absolute; left: 405px; top: 0; width: 281px; height: 871px;
    background: linear-gradient(180deg, var(--photo-mid) 0%, var(--photo-light) 35%, var(--photo-light) 70%, var(--photo-shadow) 100%);
  }
  .title-band {
    position: absolute; left: 0; top: 50px; width: 523px; height: 147px;
    background: var(--header-band);
  }
  .headline {
    position: absolute; left: 46px; top: 64px;
    color: var(--white); font-weight: 600; font-size: 38px; line-height: 52px;
    white-space: nowrap;
  }
  .headline strong { font-weight: 800; font-size: 50px; }
  .headline .line-two { font-size: 36px; }
  .audience {
    position: absolute; left: 40px; top: 214px;
    font-size: 21px; font-weight: 500; line-height: 30px; color: var(--ink-soft);
  }
  .tagline {
    position: absolute; left: 40px; top: 287px;
    font-size: 21px; font-weight: 700; line-height: 30px; color: var(--accent-red);
  }
  .sessions-tab {
    position: absolute; left: 0; top: 371px; width: 258px; height: 40px;
  }
  .sessions-tab span {
    position: absolute; left: 40px; top: 2px;
    font-family: "Oswald", sans-serif; font-weight: 500; font-size: 26px;
    color: var(--white); letter-spacing: 0.2px;
  }
  .course-facts {
    position: absolute; left: 40px; top: 422px;
    font-family: "Oswald", sans-serif; line-height: 1;
  }
  .fact { position: relative; padding-left: 30px; }
  .fact::before {
    content: ""; position: absolute; left: 2px; top: 8px;
    border-left: 15px solid var(--ink); border-top: 9px solid transparent; border-bottom: 9px solid transparent;
  }
  .fact-label { font-size: 30px; font-weight: 400; }
  .fact-value { font-size: 48px; font-weight: 500; margin-top: 2px; }
  .fact--session { color: var(--accent-red); }
  .fact--session::before { border-left-color: var(--ink); }
  .fact--start { margin-top: 14px; color: var(--ink); }
  .fact--start .fact-value { font-size: 62px; font-weight: 600; }
  .list-divider {
    position: absolute; left: 43px; top: 646px; width: 248px;
    border-top: 2px dashed var(--ink-soft);
  }
  .topic-list {
    position: absolute; left: 43px; top: 664px;
    list-style: none; font-size: 14px; font-weight: 600; line-height: 20px; color: var(--ink);
  }
  .topic-list li span { margin-right: 8px; }
  .topic-list li span::before {
    content: ""; display: inline-block; width: 8px; height: 8px; margin-right: 6px;
    border: 1.5px solid var(--ink); border-radius: 50%; vertical-align: 1px;
  }
  .course-badge { position: absolute; left: 498px; top: 345px; width: 0; height: 0; }
  .course-badge svg { position: absolute; left: -95px; top: 0; }
  .course-badge p {
    position: absolute; left: -95px; top: 68px; width: 272px; text-align: center;
    color: var(--white); font-weight: 600; font-size: 33px; line-height: 42px;
  }
  .footer-rule {
    position: absolute; left: 0; top: 869px; width: 686px; height: 4px;
    background: var(--footer-rule);
  }
  .footer {
    position: absolute; left: 0; top: 873px; width: 686px; height: 68px;
    background: var(--white);
    display: flex; align-items: center; justify-content: center;
    font-size: 18px; font-weight: 600; color: var(--ink);
  }
</style>
</head>
<body>
  <main class="poster">
    <div class="portrait-photo" role="img" aria-label="Photo of a smiling young man in glasses, short hair, white shirt and black tie"></div>

    <div class="title-band"></div>
    <h1 class="headline">How to Make Money<br><span class="line-two">In <strong>Real Estate?</strong></span></h1>

    <p class="audience">For those who have started or<br>would like to go into Real Estate</p>
    <p class="tagline">An investment in knowledge<br>opens up untold opportunities</p>

    <div class="sessions-tab">
      <svg width="258" height="40" viewBox="0 0 258 40" aria-hidden="true">
        <polygon points="0,0 258,0 244,40 0,40" fill="var(--ink)"/>
      </svg>
      <span>REMOTE SESSIONS</span>
    </div>

    <div class="course-facts">
      <div class="fact fact--session">
        <div class="fact-label">12 SESSION</div>
        <div class="fact-value">COURSE</div>
      </div>
      <div class="fact fact--start">
        <div class="fact-label">CLASSES STARTING</div>
        <div class="fact-value">JUNE 16</div>
      </div>
    </div>

    <div class="list-divider"></div>
    <ul class="topic-list">
      <li><span>A partial listing of Topics</span><span>Single-family</span></li>
      <li><span>Multifamily</span><span>Management</span></li>
      <li><span>Real Estate Concepts</span></li>
      <li><span>Real Estate law</span></li>
      <li><span>Investment properties</span></li>
      <li><span>Foreclosures</span><span>Rehab</span><span>Foreclosures</span></li>
      <li><span>Short sales</span><span>Development</span></li>
      <li><span>Finical modeling</span><span>HUD properties</span></li>
      <li><span>Due Diligence</span></li>
    </ul>

    <div class="course-badge">
      <svg width="272" height="250" viewBox="0 0 272 250" aria-hidden="true">
        <path d="M150 6 C215 -6 268 40 270 110 C272 180 225 235 160 246 C95 256 40 232 14 195 C-8 162 2 120 30 92 C65 55 100 16 150 6 Z" fill="var(--blob-red)"/>
      </svg>
      <p>Real Estate<br>Career<br>Course</p>
    </div>

    <div class="footer-rule"></div>
    <footer class="footer">www.website.com</footer>
  </main>
</body>
</html>
```